Vel CBD Pod package and logo design.

Vel is the brand name for our line of CBD Tarn style pods. I would like the logo to be designed as well as the packaging. The packaging will be the same size as the Tarn pod packaging. I would also like the box to be white and have a similar clean look just as Tarn does. My vision for the brand is very simple with black letters in a font similar to the picture attached. I would also like an animated marijuana flower that is extremely simple and also very similar to the picture attached below. Please note that I do not want the logo to be an exact copy of the example attached. I have also attached a picture of the Tarn packaging.

Although I do like my idea of the logo I am very much open to your creative ideas and will absolutely consider any other logo designs outside of my description. One final note, outside of the simple marijuana flower above the "i", I do not want the logo to scream "Marijuana" as it is a CBD product and the overt marijuana referenced brands dont fair to well to the non-marijuana user. If you have any questions, please do not hesitate to ask.

```html
<!DOCTYPE html>
<html lang="en">
<head>
<meta charset="utf-8">
<title>Vel CBD Pods – Packaging</title>
<link href="https://fonts.googleapis.com/css2?family=Oswald:wght@500&family=Josefin+Sans:wght@300;400&family=Nunito+Sans:wght@400;700&family=Cinzel:wght@500&display=swap" rel="stylesheet">
<style>
  :root {
    --backdrop: #858789;
    --panel-border: #6f7173;
    --pack-cool: #e8f5f3;
    --pack-mint: #eaf5ec;
    --slate: #5a5e7a;
    --teal: #2fb5b4;
    --leaf-teal: #3cc0bb;
    --leaf-green: #6cbf72;
    --pod-green: #66bc7e;
    --pod-dark: #4b4e49;
    --ink: #333333;
    --white: #ffffff;
  }
  * { box-sizing: border-box; margin: 0; padding: 0; }
  html, body { width: 1200px; height: 1032px; overflow: hidden; }
  body { background: var(--backdrop); position: relative; font-family: "Nunito Sans", sans-serif; }

  .pack {
    position: absolute; top: 46px; width: 548px; height: 949px;
    border: 1px solid var(--panel-border);
  }
  .pack--cool { left: 30px; background: var(--pack-cool); }
  .pack--mint { left: 605px; background: var(--pack-mint); }

  .brand-name { position: absolute; line-height: 1; white-space: nowrap; }
  .brand-name--block {
    left: 44px; top: 40px; font-family: "Oswald", sans-serif; font-weight: 500;
    font-size: 170px; letter-spacing: 2px; color: var(--slate);
  }
  .brand-name--script {
    left: 62px; top: 70px; font-family: "Josefin Sans", sans-serif; font-weight: 300;
    font-size: 150px; color: var(--ink);
  }

  .flower { position: absolute; }
  .flower--teal { left: 341px; top: 58px; width: 136px; height: 120px; border-radius: 50% 50% 40% 40%; background: radial-gradient(circle, var(--leaf-teal) 0%, rgba(60,192,187,0.25) 70%); }
  .flower--green { left: 404px; top: 30px; width: 120px; height: 104px; border-radius: 50%; background: radial-gradient(circle, var(--leaf-green) 0%, rgba(108,191,114,0.35) 70%); }
  .strain {
    position: absolute; left: 336px; top: 183px; width: 176px; text-align: center;
    font-family: "Cinzel", serif; font-weight: 500; font-size: 20px; letter-spacing: 1.5px; color: var(--ink);
  }

  .tag { position: absolute; left: 0; color: var(--white); display: flex; align-items: center; padding-left: 42px; white-space: nowrap; }
  .tag--count { top: 281px; width: 164px; height: 41px; background: var(--slate); font-weight: 700; font-size: 28px; }
  .tag--strength { top: 325px; width: 270px; height: 40px; background: var(--teal); font-weight: 400; font-size: 29px; }

  .pod-area {
    position: absolute; left: 46px; top: 431px; width: 456px; height: 203px; border-radius: 4px;
    background: linear-gradient(180deg, var(--pod-green) 0%, var(--pod-green) 46%, var(--pod-dark) 54%, var(--pod-dark) 100%);
  }

  .tagline {
    position: absolute; left: 0; width: 100%; top: 696px; text-align: center;
    font-family: "Josefin Sans", sans-serif; font-weight: 400; font-size: 21.5px; color: var(--ink);
  }
  .warning {
    position: absolute; left: 41px; top: 727px; width: 467px; height: 184px;
    border: 1.5px solid var(--ink); display: flex; flex-direction: column; justify-content: center;
    text-align: center; font-family: "Josefin Sans", sans-serif; font-weight: 400;
    font-size: 28px; line-height: 37px; letter-spacing: 3px; text-transform: uppercase; color: var(--ink);
  }
</style>
</head>
<body>

<section class="pack pack--cool">
  <div class="brand-name brand-name--block">VEL</div>
  <div class="flower flower--teal" role="img" aria-label="Simple line-drawn cannabis leaf in teal"></div>
  <div class="strain">Marijuana</div>
  <div class="tag tag--count">4 Pods</div>
  <div class="tag tag--strength">5.0% Strength</div>
  <div class="pod-area" role="img" aria-label="Row of four vape pods with green tops and dark bases"></div>
  <p class="tagline">The Alternative For Adults Smokers</p>
  <div class="warning"><span>Warning!</span><span>This product contains</span><span>nicotine. Nicotine is an</span><span>addictive chemical</span></div>
</section>

<section class="pack pack--mint">
  <div class="brand-name brand-name--script">vel</div>
  <div class="flower flower--green" role="img" aria-label="Simple geometric cannabis flower in green"></div>
  <div class="tag tag--count">4 Pods</div>
  <div class="tag tag--strength">5.0% Strength</div>
  <div class="pod-area" role="img" aria-label="Row of four vape pods with green tops and dark bases"></div>
  <p class="tagline">The Alternative For Adults Smokers</p>
  <div class="warning"><span>Warning!</span><span>This product contains</span><span>nicotine. Nicotine is an</span><span>addictive chemical</span></div>
</section>

</body>
</html>
```